Need a single page vertical flyer to include in a folder of info

Need a list of things we offer with partnerships of another company
single page easy to read.

Look at www.senrovia.com for info
include that we provide a free report from www.senrovia.com with every complete job that is linked to www.pelmarix.com for source info.

mobile services we provide
advanced driver systems (adas) calibrations
Diagnostics
Oem programming European and domestics.
collision mechanical
Wiring repair
pigtails

we service all makes and models

Email estimate to milo@b-runeworks.com for free Senrovia Scan report

important phrases, " Locally owned and operated."

"Dealership alternative."
"We help speedup your cycle time."
Phone (520) 555-0173

Target Market(s)

Business to business

Industry/Entity Type

Mobile Auto diagnostics and calibrations

Requirements
Must have
• Easy to read and to the point.
Nice to have
• Clean background with some kind of photo

```html
<!DOCTYPE html>
<html lang="en">
<head>
<meta charset="utf-8">
<title>B-Rune Works Automotive Solutions – Services Flyer</title>
<link href="https://fonts.googleapis.com/css2?family=Fira+Sans+Condensed:ital,wght@0,400;0,500;0,600;0,700;1,600&family=Archivo:wght@700&display=swap" rel="stylesheet">
<style>
  :root {
    --navy: #262158;
    --navy-deep: #17143a;
    --gold: #f5b935;
    --gold-soft: #d9a54a;
    --cream: #fff6e6;
    --white: #ffffff;
    --sky: #0aa0e2;
    --ink: #111111;
  }
  * { margin: 0; padding: 0; box-sizing: border-box; }
  html, body { width: 848px; height: 1200px; overflow: hidden; background: var(--navy-deep); }
  .flyer {
    position: relative;
    width: 848px;
    height: 1200px;
    overflow: hidden;
    background: linear-gradient(180deg, var(--navy) 0%, #2b2660 45%, #221d4f 100%);
    font-family: "Fira Sans Condensed", sans-serif;
    color: var(--white);
  }
  .backdrop { position: absolute; inset: 0; }
  .abs { position: absolute; }

  /* brand */
  .brand { left: 48px; top: 98px; width: 394px; text-align: center; }
  .brand-name {
    font-size: 64px; font-weight: 700; color: var(--gold);
    line-height: 76px; letter-spacing: 1px; white-space: nowrap;
  }
  .brand-line {
    margin-top: 12px; padding: 3px 0;
    border-top: 2px solid var(--white); border-bottom: 2px solid var(--white);
    font-size: 26px; font-weight: 600; letter-spacing: 3.5px; color: var(--white); line-height: 1.1;
    white-space: nowrap;
  }
  .brand-tag {
    margin-top: 8px; font-size: 17px; font-weight: 400; letter-spacing: 4px; color: var(--gold);
    line-height: 1; white-space: nowrap;
  }

  .estimate { left: 52px; top: 274px; }
  .estimate-label { font-size: 40px; font-weight: 500; line-height: 42px; }
  .estimate-email { font-size: 46px; font-weight: 500; color: var(--gold); line-height: 50px; margin-top: 2px; white-space: nowrap; }
  .estimate-phone { font-size: 22px; font-weight: 500; line-height: 26px; margin-top: 2px; }

  .report-note {
    left: 542px; top: 44px; width: 300px;
    font-size: 35px; font-weight: 500; line-height: 45.5px; white-space: nowrap;
  }
  .report-note .hl { color: var(--gold); }

  /* services */
  .services { left: 52px; top: 422px; }
  .services-title { font-size: 39px; font-weight: 600; letter-spacing: .5px; line-height: 1; margin-bottom: 10px; }
  .services-list { list-style: none; }
  .services-list li {
    position: relative; padding-left: 24px;
    font-size: 31px; font-weight: 500; line-height: 40px; white-space: nowrap;
  }
  .services-list li.item::before {
    content: ""; position: absolute; left: 0; top: 7px;
    width: 11px; height: 25px; background: var(--gold);
  }
  .services-list li.gap { margin-top: 8px; }

  .makes {
    left: 52px; top: 808px; width: 220px;
    font-size: 33px; font-weight: 500; line-height: 44px; color: var(--gold-soft);
  }

  .slogan {
    font-style: italic; font-weight: 600; color: var(--cream);
    font-size: 41px; line-height: 41px;
  }
  .slogan-local { left: 232px; top: 850px; width: 260px; text-align: center; }
  .slogan-dealer { left: 30px; top: 1017px; width: 240px; text-align: center; }

  .cycle {
    left: 542px; top: 1030px; padding-left: 18px;
    border-left: 9px solid var(--gold);
    font-size: 40px; font-weight: 500; line-height: 40px;
  }

  /* badge */
  .badge-pill {
    left: 556px; top: 528px; width: 200px; height: 50px;
    background: var(--white); border-radius: 25px;
    display: flex; align-items: center; justify-content: center;
    font-family: "Archivo", sans-serif; font-weight: 700; font-size: 19px; color: var(--ink);
    letter-spacing: .5px; white-space: nowrap;
  }
  .badge-text {
    left: 518px; top: 586px; width: 280px; text-align: center;
    font-size: 38px; font-weight: 500; line-height: 42px; color: var(--white); white-space: nowrap;
  }
</style>
</head>
<body>
<main class="flyer">
  <svg class="backdrop" width="848" height="1200" viewBox="0 0 848 1200" aria-hidden="true">
    <defs>
      <radialGradient id="glow" cx="0.62" cy="0.45" r="0.6">
        <stop offset="0" stop-color="#8a86b8" stop-opacity=".75"/>
        <stop offset=".55" stop-color="#5e5a9a" stop-opacity=".45"/>
        <stop offset="1" stop-color="#262158" stop-opacity="0"/>
      </radialGradient>
      <linearGradient id="bandFade" x1="0" y1="0" x2="0" y2="1">
        <stop offset="0" stop-color="#c99a4f" stop-opacity=".95"/>
        <stop offset=".7" stop-color="#c99a4f" stop-opacity=".55"/>
        <stop offset="1" stop-color="#c99a4f" stop-opacity="0"/>
      </linearGradient>
      <linearGradient id="bandSolid" x1="0" y1="0" x2="0" y2="1">
        <stop offset="0" stop-color="#cfa055" stop-opacity=".95"/>
        <stop offset="1" stop-color="#c99a4f" stop-opacity=".35"/>
      </linearGradient>
    </defs>
    <g role="img" aria-label="Photo: technician's hands using a diagnostic tablet connected by cable to a vehicle">
      <rect x="200" y="380" width="648" height="820" fill="url(#glow)"/>
    </g>
    <polygon points="52,410 333,410 60,880 0,880 0,510" fill="url(#bandFade)"/>
    <polygon points="280,840 558,840 330,1200 150,1200" fill="url(#bandSolid)" opacity=".85"/>
    <polygon points="52,1007 333,1007 140,1200 0,1200 0,1090" fill="url(#bandSolid)"/>
    <polyline points="404,462 433,462 433,804 397,804" fill="none" stroke="#ffffff" stroke-width="2"/>
    <polygon points="445,580 506,615 445,650" fill="#ffffff"/>
    <polygon fill="#0aa0e2" points="660,455 701,489 752,479 758,531 806,555 779,600 806,645 758,669 752,721 701,711 660,745 619,711 568,721 562,669 514,645 541,600 514,555 562,531 568,479 619,489"/>
  </svg>

  <header class="brand abs">
    <div class="brand-name">B-RUNE WORKS</div>
    <div class="brand-line">AUTOMOTIVE SOLUTIONS</div>
    <div class="brand-tag">ADAS DIAGNOSTICS MECHANICAL</div>
  </header>

  <section class="estimate abs">
    <p class="estimate-label">Email estimate to:</p>
    <p class="estimate-email">milo@b-runeworks.com</p>
    <p class="estimate-phone">Phone (520) 555-0173</p>
  </section>

  <p class="report-note abs">We provide a<br><span class="hl">free report</span> from<br>them with every<br>complete job<br><span class="hl">www.pelmarix.com</span><br>for source info.</p>

  <section class="services abs">
    <h2 class="services-title">OUR SERVICES</h2>
    <ul class="services-list">
      <li class="item">Advanced driver systems<br>(adas) calibrations</li>
      <li class="item gap">Diagnostics</li>
      <li class="item">Oem programming</li>
      <li class="cont">European and domestics</li>
      <li class="item">Collision mechanical</li>
      <li class="item">Wiring repair</li>
      <li class="item">Pigtails</li>
    </ul>
  </section>

  <p class="makes abs">We service all makes and models</p>

  <div class="badge-pill abs">SENROVIA SCAN</div>
  <p class="badge-text abs">Free!!<br>Senrovia Scan<br>Report</p>

  <p class="slogan slogan-local abs">Locally<br>owned and<br>operated.</p>
  <p class="slogan slogan-dealer abs">Dealership<br>alternative</p>

  <p class="cycle abs">We help<br>speedup your<br>cycle time</p>
</main>
</body>
</html>
```